I have a logo and need to design the business card and stationery.

The uploaded logo image named as FERNHOLT CONSTRUCTION which is to be replaced to FERNHOLT CONTRACTS. Kindly add below details and submit the designs- Company name- Fernholt Engineering Contracts LLP Name & Post- Varun Kelkar (Designated Partner) Address- Block No.712, Wing C, Tulsa Trade Court, Moti Lal Road, Pawar Industrial Estate, Goregaon(E), Mumbai - 400 063 Contact- +91 97410 58263 Email- varunkelkar@mailnest.example Website- www.fernholtcontracts.example Contact for Letterhead- +91-22-27481195

Hi Tanvir Haque, We are liking your Design #41927306. We have suggested some changes which are mentioned in feedback. Kindly revert with it asap to finalize this design.

Colors

Designer to choose colors to be used in the design.

```html
<!DOCTYPE html>
<html lang="en">
<head>
<meta charset="utf-8">
<title>Fernholt Contracts – Business Card</title>
<link href="https://fonts.googleapis.com/css2?family=Poppins:wght@400;500;600;700&display=swap" rel="stylesheet">
<style>
  :root{
    --bg:#1c1c1c;
    --paper:#ffffff;
    --paper-soft:#f3f3f3;
    --ink:#1f1f1f;
    --ink-mid:#3a3a3a;
    --band:#2b2b2b;
    --on-band:#ffffff;
  }
  *{margin:0;padding:0;box-sizing:border-box}
  html,body{width:1200px;height:1015px;overflow:hidden;background:var(--bg);font-family:"Poppins",sans-serif}
  .sheet{position:relative;width:1200px;height:1015px}
  .card{position:absolute;left:220px;width:760px;height:434px;background:var(--paper);box-shadow:0 10px 30px rgba(0,0,0,.5);overflow:hidden}
  .card--back{top:44px;background:linear-gradient(180deg,var(--paper),var(--paper-soft))}
  .card--front{top:537px}

  .brand{display:flex;align-items:center;gap:18px;color:var(--ink)}
  .brand__mark{width:64px;height:64px;border:9px solid var(--ink)}
  .brand__name{font-weight:700;font-size:34px;letter-spacing:1px;line-height:1}

  .card--back .brand{position:absolute;left:0;right:0;top:92px;justify-content:center}
  .company{position:absolute;left:0;right:0;top:222px;text-align:center;color:var(--ink)}
  .company__name{font-weight:700;font-size:21px;letter-spacing:.3px}
  .company__address{margin-top:10px;font-size:17px;line-height:1.5;color:var(--ink-mid)}

  .person{position:absolute;left:52px;top:64px;color:var(--ink)}
  .person__name{font-weight:700;font-size:26px;line-height:1.1}
  .person__role{font-size:15px;color:var(--ink-mid)}

  .card--front .brand{position:absolute;left:392px;top:92px}
  .card--front .brand__name{font-size:30px}
  .feature-mark{position:absolute;right:40px;top:150px;width:150px;height:150px;border:16px solid var(--ink)}

  .band{position:absolute;inset:0}
  .contacts{position:absolute;left:52px;top:268px;list-style:none;color:var(--on-band);font-size:19px}
  .contacts li{display:flex;align-items:center;gap:16px;height:34px}
  .contacts svg{width:20px;height:20px;flex:none}
</style>
</head>
<body>
<main class="sheet">

  <section class="card card--back" aria-label="Card back">
    <div class="brand">
      <span class="brand__mark"></span>
      <span class="brand__name">FERNHOLT CONTRACTS</span>
    </div>
    <div class="company">
      <p class="company__name">FERNHOLT ENGINEERING CONTRACTS LLP</p>
      <p class="company__address">Block No.712, Wing C, Tulsa Trade Court, Moti Lal Road,<br>Pawar Industrial Estate, Goregaon(E), Mumbai - 400 063</p>
    </div>
  </section>

  <section class="card card--front" aria-label="Card front">
    <svg class="band" viewBox="0 0 760 434" aria-hidden="true">
      <path d="M0 250 H330 V160 H590 V382 H0 Z" fill="var(--band)"/>
    </svg>
    <div class="person">
      <p class="person__name">VARUN KELKAR</p>
      <p class="person__role">Designated Partner</p>
    </div>
    <div class="brand">
      <span class="brand__name">FERNHOLT CONTRACTS</span>
    </div>
    <span class="feature-mark"></span>
    <ul class="contacts">
      <li>
        <svg viewBox="0 0 20 20" aria-hidden="true"><rect x="1" y="1" width="18" height="18" rx="3" fill="none" stroke="#fff" stroke-width="1.6"/><path d="M7 5 l2 3 -1.2 1.2 a7 7 0 0 0 3 3 L12 11 l3 2 -1 2 c-5 0-9-4-9-9z" fill="#fff"/></svg>
        <span>+91 97410 58263</span>
      </li>
      <li>
        <svg viewBox="0 0 20 20" aria-hidden="true"><rect x="1" y="4" width="18" height="12" fill="none" stroke="#fff" stroke-width="1.6"/><path d="M1 4 L10 11 L19 4" fill="none" stroke="#fff" stroke-width="1.6"/></svg>
        <span>varunkelkar@mailnest.example</span>
      </li>
      <li>
        <svg viewBox="0 0 20 20" aria-hidden="true"><circle cx="10" cy="10" r="8.5" fill="none" stroke="#fff" stroke-width="1.6"/><ellipse cx="10" cy="10" rx="3.8" ry="8.5" fill="none" stroke="#fff" stroke-width="1.2"/><path d="M1.5 10 H18.5 M3 6 H17 M3 14 H17" stroke="#fff" stroke-width="1.2"/></svg>
        <span>www.fernholtcontracts.example</span>
      </li>
    </ul>
  </section>

</main>
</body>
</html>
```